Movra Business Card

We need a business card design for Movra, an independent sewing pattern company based near Quebec City. We make patterns for children and adults and specialize in everything other big pattern brands won't tackle: activewear, sportswear (figure skating, gymnastics), underwear. We are a small business and would like our cards to be stylish and fun, not corporate looking.

Target Market(s)

Educated women 35-55 who sew for themselves or their family. They like fashion and sew to be different and make clothes that fit them like a glove, not necessarily to save money.

Industry/Entity Type

Small Business

Requirements
Must have
• Movra logo, contact info:

Colette Darvaux, president & founder / présidente et fondatrice

Movra
3915 rue Fontaine
Val-Corbin NB H2K4P9
Canada

info@movra.com
www.movra.com
Nice to have
• Sewing/fashion-related graphics. You can use any pattern cover available on www.movra.com for inspiration. Stylish illustrations / sketches inspired by existing garments we have would be great. Something showing pattern grading could also be an option.

The design can be on one- or two-sided. We are open to variations (e.g. 4-5 different backs for a given card)
Should not have
• nothing too cartoonish or girly please :) we prefer something timeless, fashion-forward.

```html
<!DOCTYPE html>
<html lang="en">
<head>
<meta charset="utf-8">
<title>Movra Business Card</title>
<link rel="stylesheet" href="https://fonts.googleapis.com/css2?family=Source+Sans+3:wght@400;600&display=swap">
<style>
  :root {
    --page-bg: #e9e7e4;
    --card-white: #f1f1f0;
    --card-brown: #4a2c30;
    --bead-blue: #80b7cf;
    --bead-cream: #e6e2dc;
    --ink: #222222;
    --rule-blue: #8fbfd4;
  }
  * { margin: 0; padding: 0; box-sizing: border-box; }
  html, body {
    width: 1200px;
    height: 900px;
    overflow: hidden;
    background: var(--page-bg);
    font-family: "Source Sans 3", sans-serif;
  }
  .canvas {
    position: relative;
    width: 1200px;
    height: 900px;
  }
  .card {
    position: absolute;
    top: 300px;
    width: 520px;
    height: 297px;
    overflow: hidden;
    box-shadow: 0 6px 18px rgba(0, 0, 0, 0.18);
  }
  .card--back {
    left: 50px;
    background: var(--card-brown);
  }
  .card--front {
    left: 630px;
    background: var(--card-white);
  }
  .pattern-area {
    position: absolute;
    inset: 0;
    width: 100%;
    height: 100%;
  }
  .brand-name {
    position: absolute;
    font-weight: 600;
    letter-spacing: 0.02em;
  }
  .card--back .brand-name {
    top: 118px;
    left: 0;
    width: 100%;
    text-align: center;
    font-size: 48px;
    color: var(--bead-blue);
  }
  .card-details {
    position: absolute;
    top: 38px;
    left: 0;
    width: 100%;
    text-align: center;
    color: var(--ink);
  }
  .card-details .brand-name {
    position: static;
    display: block;
    font-size: 44px;
    line-height: 1;
    margin-bottom: 22px;
    color: var(--ink);
  }
  .person-name {
    font-size: 20px;
    font-weight: 400;
    letter-spacing: 0.04em;
    line-height: 1.2;
  }
  .person-title {
    font-size: 14px;
    line-height: 1.3;
  }
  .divider {
    width: 270px;
    height: 1px;
    margin: 10px auto 9px;
    background: var(--rule-blue);
    border: 0;
  }
  .company {
    font-size: 12px;
    font-weight: 600;
    line-height: 1.3;
  }
  .contact {
    font-style: normal;
    font-size: 13.5px;
    line-height: 1.35;
  }
</style>
</head>
<body>
<main class="canvas">

  <section class="card card--back" aria-label="Business card back">
    <svg class="pattern-area" viewBox="0 0 520 297" role="img" aria-label="Strands of light blue and cream beads draped across the brown card">
      <defs>
        <linearGradient id="backStrands" x1="0" y1="0" x2="1" y2="1">
          <stop offset="0" stop-color="#4a2c30"/>
          <stop offset="0.5" stop-color="#5a4a52"/>
          <stop offset="1" stop-color="#4a2c30"/>
        </linearGradient>
      </defs>
      <rect width="520" height="297" fill="url(#backStrands)"/>
    </svg>
    <span class="brand-name">Movra</span>
  </section>

  <section class="card card--front" aria-label="Business card front">
    <svg class="pattern-area" viewBox="0 0 520 297" role="img" aria-label="Light blue bead strands curving in from the card edges">
      <defs>
        <linearGradient id="strandLeft" x1="0" y1="1" x2="1" y2="0">
          <stop offset="0" stop-color="#80b7cf" stop-opacity="0.55"/>
          <stop offset="1" stop-color="#80b7cf" stop-opacity="0"/>
        </linearGradient>
        <linearGradient id="strandRight" x1="1" y1="0" x2="0" y2="1">
          <stop offset="0" stop-color="#80b7cf" stop-opacity="0.55"/>
          <stop offset="1" stop-color="#80b7cf" stop-opacity="0"/>
        </linearGradient>
      </defs>
      <path d="M0 297 L0 180 Q60 170 130 120 L150 140 Q80 200 40 297 Z" fill="url(#strandLeft)"/>
      <path d="M520 0 L520 150 Q470 130 430 60 Q420 30 430 0 Z" fill="url(#strandRight)"/>
    </svg>

    <div class="card-details">
      <span class="brand-name">Movra</span>
      <h1 class="person-name">COLETTE DARVAUX</h1>
      <p class="person-title">President &amp; founder / Présidente et fondatrice</p>
      <hr class="divider">
      <p class="company">Movra</p>
      <address class="contact">
        3915 rue Fontaine, Val-Corbin NB H2K4P9, Canada<br>
        info@movra.com<br>
        www.movra.com
      </address>
    </div>
  </section>

</main>
</body>
</html>
```